My Bramblewood Interiors llc fliers project

A flyer that will be direct mailed to customers. feel free to play with wording this is what i have now. I wlil include every service i offer in must haves and feel free to run a footer stating all my services
" My background, I'm Oren Vashtakar, I was born Into this business, Its what I know. So if your tired of waiting for weeks before your kitchen gets completed, as happens with other companies. If your tired of dealing with unreliable contractors deal with me. I'm so confident in my work, here are the numbers to previous customer. Mrs.Pelham-703-555-0142. Mr.Castellano 703-555-0187. They will tell you I can provide you that dream kitchen and countertop installed, within a week. Mention this flyer to receive an additional 10% discoun
BrambleWood Interiors llc
5819 fernwick dale CT
Falls church VA,22042
703-555-0163
Ovashtakar@mailbrook.net"

Target Market(s)

high income household income looking to get interior work done,

Industry/Entity Type

Church

Font styles to use
Serif

Requirements
Must have
• granite and marble kitchen and bathroom fabrication and install
• any flooring, hardwood, marble, carpet, laminate, install
• Kitchen cabinet design and install
• Bathroom remodeling
Nice to have
• an easy to read flyer that will give customers the info to reach me and understand what they do, if I put to much then reduce it.

```html
<!DOCTYPE html>
<html lang="en">
<head>
<meta charset="utf-8">
<title>Bramblewood Interiors LLC – Flyer and Postcard</title>
<link rel="stylesheet" href="https://fonts.googleapis.com/css2?family=Open+Sans:ital,wdth,wght@0,75..100,300..800;1,75..100,300..800&display=swap">
<style>
:root{
  --backdrop:#e9e6e1;
  --paper:#ffffff;
  --ink:#4a4a4a;
  --ink-dark:#333333;
  --slate:#2b2b2b;
  --slate-mid:#4d4d4d;
  --slate-light:#6e6e6e;
  --orange:#f08a1c;
  --rule:#9a9a9a;
}
*{margin:0;padding:0;box-sizing:border-box}
html,body{width:1200px;height:673px;overflow:hidden}
body{background:var(--backdrop);font-family:"Open Sans",Arial,sans-serif;color:var(--ink);position:relative}

/* ---------- Flyer ---------- */
.flyer{position:absolute;left:35px;top:40px;width:450px;height:573px;background:var(--paper);box-shadow:0 3px 10px rgba(0,0,0,.35);overflow:hidden}
.flyer-stone{position:absolute;left:0;top:0;width:165px;height:520px;background:linear-gradient(160deg,#3a3a3a 0%,#6b6b6b 35%,#2e2e2e 60%,#555 85%,#262626 100%)}
.discount-seal{position:absolute;left:27px;top:50px;width:92px;height:92px;border-radius:50%;background:var(--orange);display:flex;align-items:center;justify-content:center}
.discount-seal .inner{width:74px;height:74px;border-radius:50%;background:var(--paper);display:flex;flex-direction:column;align-items:center;justify-content:center;text-align:center;color:var(--ink-dark)}
.discount-seal .pct{font-weight:800;font-size:19px;line-height:1;border-bottom:1px solid var(--ink-dark);padding-bottom:2px;margin-bottom:2px}
.discount-seal .note{font-style:italic;font-weight:700;font-size:7px;line-height:1.15}
.flyer-title{position:absolute;left:185px;top:50px;font-weight:700;font-stretch:80%;font-size:35px;line-height:1.17;color:var(--ink)}
.service-list{position:absolute;left:177px;top:160px;list-style:none;font-stretch:85%;font-size:16.5px;line-height:21px;color:var(--ink-dark)}
.service-list li{padding-left:12px;text-indent:-12px;margin-bottom:16px}
.service-list li::before{content:"» ";}
.photo{position:absolute;top:365px;height:115px}
.photo-1{left:5px;width:142px;background:linear-gradient(135deg,#6b4a2c,#a7804f 50%,#3e2a1a)}
.photo-2{left:155px;width:137px;background:linear-gradient(135deg,#4a2e1b,#8d5a33 50%,#c29a6a)}
.photo-3{left:300px;width:140px;background:linear-gradient(135deg,#c9a574,#e8dcc0 50%,#8e6a3e)}
.flyer-address{position:absolute;right:20px;top:497px;font-stretch:85%;font-size:13px;color:var(--ink-dark)}
.flyer-footer{position:absolute;left:0;bottom:0;width:100%;height:55px;background:var(--slate);border-top:2px solid var(--orange);display:flex;align-items:center;justify-content:space-between;padding:0 18px 0 14px;color:var(--paper)}
.footer-phone{display:flex;align-items:center;gap:8px;font-weight:700;font-stretch:85%;font-size:22px}
.footer-email{font-stretch:85%;font-size:13px}

/* ---------- Postcard ---------- */
.postcard{position:absolute;left:585px;top:170px;width:572px;height:443px;background:var(--paper);box-shadow:0 3px 10px rgba(0,0,0,.35);overflow:hidden}
.postcard-topband{position:absolute;left:0;top:0;width:100%;height:8px;background:var(--slate);border-bottom:2px solid var(--orange)}
.postcard-name{position:absolute;left:9px;top:28px;font-weight:700;font-stretch:82%;font-size:20px;line-height:23px;color:var(--ink)}
.postcard-call{position:absolute;left:130px;top:30px;width:135px;text-align:right;font-style:italic;font-weight:700;font-stretch:85%;font-size:8.5px;line-height:11px;color:var(--ink-dark)}
.postcard-phone{position:absolute;left:138px;top:52px;display:flex;align-items:center;gap:6px;font-weight:700;font-stretch:85%;font-size:16px;color:var(--ink-dark)}
.stamp-box{position:absolute;left:448px;top:37px;width:90px;height:71px;border:1px solid var(--rule)}
.letter{position:absolute;left:15px;top:96px;width:270px;font-style:italic;font-weight:700;font-stretch:85%;font-size:11px;line-height:14px;color:var(--ink-dark)}
.letter p{margin-bottom:11px}
.letter .refs{list-style:none;padding-left:8px}
.letter .refs li::before{content:"• ";}
.divider{position:absolute;left:285px;top:90px;width:1px;height:262px;background:var(--rule)}
.address-line{position:absolute;left:320px;width:216px;height:1px;background:var(--rule)}
.postcard-stone{position:absolute;left:0;bottom:0;width:100%;height:56px;background:linear-gradient(160deg,#2a2a2a 0%,#555 40%,#2c2c2c 70%,#4a4a4a 100%);border-top:2px solid var(--orange)}
</style>
</head>
<body>

<section class="flyer">
  <div class="flyer-stone" role="img" aria-label="Dark slate stone texture"></div>
  <div class="discount-seal">
    <div class="inner">
      <span class="pct">10%</span>
      <span class="note">Discount<br>With This Flyer</span>
    </div>
  </div>
  <h1 class="flyer-title">BRAMBLEWOOD<br>INTERIORS LLC</h1>
  <ul class="service-list">
    <li>Granite And Marble Kitchen And Bathroom Fabrication And Install</li>
    <li>Any Flooring, Hardwood, Marble, Carpet, Laminate</li>
    <li>Kitchen Cabinet Design And Install</li>
    <li>Bathroom Remodeling</li>
  </ul>
  <div class="photo photo-1" role="img" aria-label="Kitchen with granite countertop and stone wall"></div>
  <div class="photo photo-2" role="img" aria-label="Kitchen with wood cabinets and island with pendant lights"></div>
  <div class="photo photo-3" role="img" aria-label="Bright kitchen with oak cabinets and appliances"></div>
  <p class="flyer-address">5819 Fernwick Dale Ct&nbsp; Falls Church VA,22042</p>
  <footer class="flyer-footer">
    <span class="footer-phone">
      <svg width="30" height="24" viewBox="0 0 30 24" aria-hidden="true"><path d="M3 9c0-4 5-6 12-6s12 2 12 6v2h-6V8c-2-1-10-1-12 0v3H3z" fill="#fff"/><path d="M8 12h14l4 10H4z" fill="#fff"/><circle cx="15" cy="17" r="3" fill="#2b2b2b"/></svg>
      703-555-0163
    </span>
    <span class="footer-email">ovashtakar@mailbrook.net</span>
  </footer>
</section>

<section class="postcard">
  <div class="postcard-topband"></div>
  <h2 class="postcard-name">BRAMBLEWOOD<br>INTERIORS LLC</h2>
  <p class="postcard-call">Call us for a free<br>evaluation and reduced pricing!</p>
  <p class="postcard-phone">
    <svg width="22" height="18" viewBox="0 0 30 24" aria-hidden="true"><path d="M3 9c0-4 5-6 12-6s12 2 12 6v2h-6V8c-2-1-10-1-12 0v3H3z" fill="#333"/><path d="M8 12h14l4 10H4z" fill="#333"/><circle cx="15" cy="17" r="3" fill="#fff"/></svg>
    703-555-0163
  </p>
  <div class="stamp-box"></div>
  <div class="letter">
    <p>Dear Neighbor,</p>
    <p>I'm Oren Vashtakar, I was born Into this business, Its what I know. So if your tired of waiting for weeks before your kitchen gets completed, as happens with other companies. If your tired of dealing with unreliable contractors deal with me.<br>I'm so confident in my work, here are the numbers to previous customer.</p>
    <ul class="refs" style="margin-top:-11px">
      <li>Mrs. Pelham&nbsp; 703-555-0142</li>
      <li>Mr. Castellano&nbsp; 703-555-0187</li>
    </ul>
    <p>They will tell you I can provide you that dream kitchen and countertop installed, within a week.</p>
    <p>Mention this flyer to receive an additional 10% discount.</p>
    <p>Sincerely,<br>Oren Vashtakar</p>
  </div>
  <div class="divider"></div>
  <div class="address-line" style="top:227px"></div>
  <div class="address-line" style="top:267px"></div>
  <div class="address-line" style="top:307px"></div>
  <div class="postcard-stone" role="img" aria-label="Dark slate stone texture band"></div>
</section>

</body>
</html>
```